Need a web site design for a moving company

We need to re-design our website for our moving company based in New York. Our current web site (brightcartageusa.com) is very inconvenient for our customers to navigate and finding what they are looking for. We would like a web site which can have the customers fill up the Free Moving Quote after browsing it. So we want you to be creative with overall design and a quote form. We would love to target different locations, so we want our customers to be able to switch conveniently accordingly where they are located. We have a rateloop page with testimonials, which we wanted to be there as well (not just a text, and name. Boxes with pictures, profiles, just something creative and attractive). Attached is the logo, with two options(brightcart -blue and brightcart - orange, so the colors can be used accordingly or you can use your own colors if needed (if looks the best). If surfing the inner pages, we want our customers to be able to submit a quote request if needed.

Menu:
Home Services Moving Tips Testimonials About FAQ Blog Contact Us (doesn't have to be in order)

Inner Pages:
Services, Moving Tips, Testimonials, About, FAQ, Blog (moving quote is not necessary), Contact Us

Websites as references:
fetchporters.com
holdroomly.com
calmhaulers.com
tinytruckers.com.au
cityvanline.com
finchhaulage.co.uk
shiftforus.com

Reason: We are not in rush and really need someone who can read our brief throughout. We are looking for a new web site design. It doesn't have to an updated version of our current website as most of the submitted designs are. Also not all the content from a current website should be placed into a new one (depending on a style of a new layout or design you can partially copy paste some of the content). You can be as much creative as you can, making it clean looking, flat color with attractive user interface. If a menu is too long, we can skip some of them and place them in footer. The main things we are concerned about are quote form, option of location look up (switch between locations) and reviews (at least some part of the page should be dedicated to it). If you have any questions or if our brief is not clear, please let us know about it, Thank you

Industry/Entity Type

Moving Company

```html
<!DOCTYPE html>
<html lang="en">
<head>
<meta charset="utf-8">
<title>Brightcart Movers</title>
<link href="https://fonts.googleapis.com/css2?family=Open+Sans:wght@400;600;700&display=swap" rel="stylesheet">
<style>
:root{
  --red:#e9485a;
  --navy:#1f3f66;
  --blue:#2b6cb0;
  --hero-a:#7a9bbd;
  --hero-b:#3d6690;
  --grey-bg:#ececec;
  --text:#555;
  --footer:#2b2b2b;
  --footer-line:#444;
  --skyline:#8a8a8a;
}
*{box-sizing:border-box;margin:0;padding:0}
html,body{width:672px;height:1200px;overflow:hidden;background:#fff}
body{font-family:"Open Sans",Arial,sans-serif;color:var(--text);font-size:8px;position:relative}

.header{position:absolute;top:0;left:0;width:672px;height:68px;background:#fff;border-bottom:3px solid var(--red)}
.brand{position:absolute;left:28px;top:23px;display:flex;align-items:center;gap:7px}
.brand-mark{width:18px;height:18px;background:var(--red)}
.brand-name{font-weight:700;font-size:15px;color:var(--red);letter-spacing:.3px;line-height:18px}
.nav{position:absolute;right:6px;top:0;display:flex;align-items:flex-start}
.nav a{font-size:10px;color:#555;text-decoration:none;padding:28px 7px 10px;line-height:12px}
.nav a.active{background:var(--red);color:#fff}

.hero{position:absolute;top:71px;left:0;width:672px;height:325px;background:linear-gradient(160deg,var(--hero-a),var(--hero-b))}
.hero h1{position:absolute;top:60px;width:100%;text-align:center;color:#fff;font-weight:600;font-size:23px;line-height:30px;letter-spacing:.3px}
.arrow{position:absolute;top:110px;width:20px;height:34px;background:rgba(0,0,0,.35);display:flex;align-items:center;justify-content:center}
.arrow.left{left:0}.arrow.right{right:0}
.dots{position:absolute;top:228px;left:0;width:100%;display:flex;justify-content:center;gap:3px}
.dots span{width:22px;height:3px;background:rgba(255,255,255,.6)}
.dots span.on{background:var(--red)}

.quote{position:absolute;top:330px;left:58px;width:570px;height:66px}
.quote-label{position:absolute;left:0;top:0;height:26px;width:160px;background:var(--navy);color:#fff;font-size:11px;font-weight:600;line-height:14px;padding:5px 8px;border-bottom:3px solid var(--red)}
.quote-type{position:absolute;left:160px;top:4px;height:22px;right:0;background:rgba(255,255,255,.55);display:flex;align-items:center;gap:16px;padding-left:22px;font-size:9px;color:#222}
.quote-type i{display:inline-block;width:9px;height:9px;border:1px solid #777;background:#fff;margin-right:4px;vertical-align:-1px}
.quote-type i.on{background:var(--navy)}
.quote-fields{position:absolute;left:0;top:26px;width:570px;height:30px;background:#fff;display:flex;align-items:center;gap:6px;padding-left:6px;border-bottom:3px solid var(--navy)}
.field{height:18px;border:1px solid #ccc;font-size:8px;line-height:10px;color:#777;padding:3px 4px;position:relative}
.field.sel::after{content:"";position:absolute;right:4px;top:7px;border:3px solid transparent;border-top-color:#666}
.quote-submit{margin-left:auto;height:30px;width:96px;background:var(--blue);color:#fff;font-weight:700;font-size:10px;display:flex;align-items:center;justify-content:center}

.services{position:absolute;top:414px;left:0;width:672px;height:238px;background:var(--grey-bg)}
.cards{position:absolute;left:51px;top:14px;display:flex;gap:10px}
.card{width:135px;height:208px;background:#fff;position:relative}
.card-photo{width:135px;height:100px}
.card h3{font-size:10px;font-weight:400;color:#333;padding:8px 6px 3px;line-height:12px;height:36px}
.card p{font-size:6px;line-height:8px;padding:0 6px;color:#888}
.btn-more{position:absolute;bottom:8px;left:50%;transform:translateX(-50%);background:var(--red);color:#fff;font-size:7px;line-height:9px;padding:3px 12px}

.newsletter{position:absolute;top:656px;left:0;width:672px;height:88px;background:var(--red);color:#fff}
.newsletter svg{position:absolute;left:64px;top:33px}
.newsletter h2{position:absolute;left:96px;top:33px;font-size:15px;line-height:20px;font-weight:400}
.newsletter p{position:absolute;left:300px;top:28px;width:130px;font-size:7px;font-weight:600;line-height:9px}
.nl-input{position:absolute;left:442px;top:36px;width:118px;height:16px;background:#fff;color:#999;font-size:7px;line-height:10px;padding:3px 5px}
.nl-btn{position:absolute;left:560px;top:36px;width:52px;height:16px;background:var(--blue);font-size:7px;line-height:10px;text-align:center;padding-top:3px}

.welcome{position:absolute;top:744px;left:0;width:672px;height:156px;background:#fff}
.welcome-art{position:absolute;left:58px;top:24px;width:92px;height:118px}
.welcome h2{position:absolute;left:160px;top:28px;font-size:14px;line-height:18px;font-weight:400;color:#444}
.welcome h2 span{color:var(--red)}
.welcome p{position:absolute;left:160px;top:52px;width:200px;font-size:6px;line-height:8px;color:#888}
.read-more{position:absolute;left:318px;top:124px;background:var(--red);color:#fff;font-size:7px;line-height:9px;padding:3px 8px}
.video{position:absolute;left:386px;top:24px;width:230px;height:118px;background:#2a2a2a}
.video-screen{position:absolute;inset:0 0 14px 0;background:linear-gradient(150deg,#4a4a4a,#1c1c1c)}
.video-bar{position:absolute;left:0;bottom:0;width:100%;height:14px;background:#111;display:flex;align-items:center;gap:6px;padding:0 6px}
.video-bar .track{flex:1;height:3px;background:#555}
.video-bar b{width:6px;height:6px;background:#bbb}

.skyline{position:absolute;top:930px;left:0;width:672px;height:56px;background:linear-gradient(to bottom,rgba(138,138,138,.35),var(--skyline))}

.footer{position:absolute;top:986px;left:0;width:672px;height:200px;background:var(--footer);color:#ccc;border-top:3px solid var(--red)}
.footer h4{font-size:9px;line-height:12px;font-weight:600;color:#fff;margin-bottom:8px;letter-spacing:.3px}
.col{position:absolute;top:12px}
.col-social{left:72px;width:140px}
.socials{display:flex;gap:6px;margin-bottom:14px}
.socials span{width:20px;height:20px;border-radius:50%;background:var(--blue)}
.col-social .post{font-size:7px;color:#fff;margin-bottom:4px}
.col-social p{font-size:6px;line-height:8px;color:#999}
.col-ads{left:254px;width:150px}
.col-ads li{list-style:none;font-size:6px;line-height:8px;color:#aaa;border-bottom:1px solid var(--footer-line);padding:3px 0 3px 6px}
.col-contact{left:452px;width:150px}
.f-input{width:150px;height:14px;background:#fff;margin-bottom:5px;font-size:6px;line-height:9px;color:#999;padding:2px 4px}
.f-input.msg{height:50px}
.f-submit{margin-left:auto;width:42px;height:14px;background:var(--blue);color:#fff;font-size:7px;line-height:10px;text-align:center;padding-top:2px}
.footer-strip{position:absolute;top:1186px;left:0;width:672px;height:14px;background:var(--red)}
</style>
</head>
<body>
<header class="header">
  <div class="brand"><span class="brand-mark"></span><span class="brand-name">BRIGHTCART MOVERS</span></div>
  <nav class="nav">
    <a class="active">Home</a><a>Services</a><a>Moving Tips</a><a>Testimonials</a><a>About</a><a>FAQ</a><a>Blog</a><a>Contact Us</a>
  </nav>
</header>

<section class="hero" role="img" aria-label="Photo of a white moving truck on the road under a blue sky">
  <h1>WHEN YOU MOVE WITH US,<br>IT'S ALMOST FUN</h1>
  <div class="arrow left"><svg width="8" height="12"><path d="M7 1 2 6l5 5" stroke="#fff" stroke-width="2" fill="none"/></svg></div>
  <div class="arrow right"><svg width="8" height="12"><path d="M1 1l5 5-5 5" stroke="#fff" stroke-width="2" fill="none"/></svg></div>
  <div class="dots"><span></span><span class="on"></span><span></span></div>
</section>

<form class="quote">
  <div class="quote-label">GET A FREE QUOTE NOW</div>
  <div class="quote-type"><label><i class="on"></i>Residential</label><label><i></i>Commercial</label></div>
  <div class="quote-fields">
    <div class="field" style="width:100px">Name</div>
    <div class="field sel" style="width:100px">Phone #</div>
    <div class="field sel" style="width:70px">Move From</div>
    <div class="field sel" style="width:70px">Move To</div>
    <div class="field sel" style="width:40px">Date</div>
    <div class="quote-submit">SUBMIT</div>
  </div>
</form>

<section class="services">
  <div class="cards">
    <article class="card">
      <div class="card-photo" role="img" aria-label="Photo of a family moving into their new home" style="background:linear-gradient(135deg,#c9b79a,#8a7a64)"></div>
      <h3>Residential Moving</h3>
      <p>We pack, load and deliver your home goods with care, on time and at a fair and clear price.</p>
      <span class="btn-more">More</span>
    </article>
    <article class="card">
      <div class="card-photo" role="img" aria-label="Photo of movers carrying office boxes" style="background:linear-gradient(135deg,#7c8fa6,#3e4f66)"></div>
      <h3>Commercial Moving</h3>
      <p>Office moves planned around your schedule so your team is back to work with no lost days.</p>
      <span class="btn-more">More</span>
    </article>
    <article class="card">
      <div class="card-photo" role="img" aria-label="Photo of a moving truck on a highway" style="background:linear-gradient(135deg,#8fb2d6,#4a6f96)"></div>
      <h3>Interstate/Long Distance Moves</h3>
      <p>Long distance moves across states with tracked trucks and one crew from start to finish.</p>
      <span class="btn-more">More</span>
    </article>
    <article class="card">
      <div class="card-photo" role="img" aria-label="Photo of stacked cardboard moving boxes" style="background:linear-gradient(135deg,#d9bf92,#a88455)"></div>
      <h3>Moving Supplies</h3>
      <p>Boxes, tape, wrap and covers in every size, ready to pick up or delivered to your door.</p>
      <span class="btn-more">More</span>
    </article>
  </div>
</section>

<section class="newsletter">
  <svg width="24" height="20" viewBox="0 0 24 20"><path d="M1 9 23 1 17 19 11 12Z M11 12 23 1" fill="none" stroke="#fff" stroke-width="1.5" stroke-linejoin="round"/></svg>
  <h2>Subscribe To Newsletter</h2>
  <p>Get moving tips, seasonal deals and local news sent to your inbox.</p>
  <div class="nl-input">Email</div>
  <div class="nl-btn">Submit</div>
</section>

<section class="welcome">
  <div class="welcome-art" role="img" aria-label="Illustration of a mover carrying a stack of boxes" style="background:linear-gradient(160deg,#7fa7cf,#d9b27a)"></div>
  <h2>Welcome to <span>Brightcart Movers</span></h2>
  <p>We are a New York moving company that makes every move simple. Our trained crews handle homes, offices and long distance moves with the same care. From the first free quote to the last box set down, you get one team, clear prices and friendly service. Pick your location, tell us where you are going and we will plan the rest for you.</p>
  <span class="read-more">Read More</span>
  <div class="video" role="img" aria-label="Company introduction video player">
    <div class="video-screen"></div>
    <div class="video-bar"><b></b><div class="track"></div><b></b><b></b></div>
  </div>
</section>

<div class="skyline" role="img" aria-label="Grey silhouette of the New York city skyline"></div>

<footer class="footer">
  <div class="col col-social">
    <h4>SOCIAL LINKS</h4>
    <div class="socials"><span></span><span></span><span></span></div>
    <h4>BLOGS</h4>
    <div class="post">Post Title</div>
    <p>Short notes on packing, planning and settling in after your move.</p>
  </div>
  <div class="col col-ads">
    <h4>ADVERTISE WITH US</h4>
    <ul>
      <li>Local moving partners</li><li>Storage and warehouse</li><li>Packing supply shops</li><li>Home cleaning services</li><li>Real estate agents</li><li>Truck rental deals</li><li>Insurance for movers</li><li>Furniture assembly</li><li>Pet moving help</li><li>Become a partner</li>
    </ul>
  </div>
  <div class="col col-contact">
    <h4>CONTACT US</h4>
    <div class="f-input">Name</div>
    <div class="f-input">Email</div>
    <div class="f-input msg">Message</div>
    <div class="f-submit">Submit</div>
  </div>
</footer>
<div class="footer-strip"></div>
</body>
</html>
```